training slide

We have an existing PPT template.

I am just looking for someone to make the attached slides better looking. If that goes well we have a whole bunch of presentations that need formatting in a similar style. Our customer base is made up of pharmaceutical and healthcare companies. we charge high end consultancy prices and it is very important our production value reflects this level of quality. We are not attached to the current PPT template and if anyone wants to re-visit that we would be very keen to see any ideas. We do however like our kelOrvanta logo but you can lose the energy, experience etc.

Industry/Entity Type

Training

```html
<!DOCTYPE html>
<html lang="en">
<head>
<meta charset="utf-8">
<title>kelOrvanta – Training Slides</title>
<link href="https://fonts.googleapis.com/css2?family=Caladea:ital,wght@0,400;0,700;1,700&display=swap" rel="stylesheet">
<style>
:root{
  --page:#ffffff;
  --plum-deep:#3f0a31;
  --plum:#7a0b58;
  --magenta:#d0078b;
  --magenta-bright:#ee0aa2;
  --band-shade:rgba(38,4,28,0.58);
  --footer:#0a0a0a;
  --ink-light:#ffffff;
  --ink-soft:#f3e3ee;
  --brand-pink:#ff1aa8;
}
*{margin:0;padding:0;box-sizing:border-box}
html,body{width:1200px;height:849px;overflow:hidden;background:var(--page)}
body{position:relative;font-family:"Caladea",Georgia,serif;color:var(--ink-light)}

.slide{
  position:absolute;width:483px;height:361px;overflow:hidden;
  background:linear-gradient(112deg,var(--plum-deep) 0%,var(--plum) 30%,var(--magenta) 68%,var(--magenta-bright) 100%);
}
.slide--title{left:85px;top:37px}
.slide--profile{left:638px;top:37px}
.slide--mission{left:85px;top:426px}
.slide--values{left:638px;top:426px}

.lower-band{position:absolute;left:0;right:0;top:240px;height:82px;background:var(--band-shade)}
.footer{position:absolute;left:0;right:0;bottom:0;height:39px;background:var(--footer)}
.footer-brand{position:absolute;left:25px;top:9px;font-size:17px;color:var(--brand-pink);letter-spacing:.2px}
.footer-url{position:absolute;right:38px;top:13px;font-size:10.5px;color:var(--ink-light)}
.slide--title .footer-url{left:188px;right:auto;color:var(--brand-pink)}

.page-number{position:absolute;right:36px;top:6px;width:16px;height:12px;background:var(--ink-light);color:#222;font-size:9px;line-height:12px;text-align:center;font-weight:700}
.slide-heading{position:absolute;left:57px;top:22px;font-size:20px;font-weight:700;font-style:italic}

.hero-brand{position:absolute;left:264px;top:54px;font-size:34px;color:var(--ink-light);letter-spacing:.3px}
.tagline{position:absolute;right:38px;top:108px;font-size:11px;color:var(--ink-light)}
.presenter{position:absolute;left:74px;top:264px;font-size:12.5px;font-weight:700;line-height:1.05}
.presenter-date{display:block;font-size:8.5px;padding-left:5px}

.credential-list{position:absolute;left:84px;top:91px;list-style:none;font-size:11px}
.credential-list li{height:29.5px;color:var(--ink-soft)}
.tick::before{content:"\2713";margin-right:1px}

.mission-statement{position:absolute;left:0;width:466px;top:109px;text-align:center;font-size:11px;line-height:30.5px;color:var(--ink-soft)}

.value{position:absolute;top:110px;width:120px}
.value--energy{left:78px}
.value--credibility{left:198px}
.value--relationships{left:323px}
.value-mark{width:48px;height:48px;border-radius:50%;background:var(--ink-light)}
.value--energy .value-mark{margin-left:8px}
.value--credibility .value-mark{margin-left:10px}
.value--relationships .value-mark{margin-left:10px}
.value-name{margin-top:20px;font-size:11.5px;font-weight:700;margin-left:2px}
.value--credibility .value-name{margin-left:0}
.value-traits{list-style:none;margin-top:15px;font-size:10px;line-height:14.5px;color:var(--ink-soft)}
.value-traits li::before{content:"\2713";margin-right:4px}
</style>
</head>
<body>

<section class="slide slide--title">
  <div class="hero-brand">kelOrvanta</div>
  <p class="tagline">Energy, Experience, Enlightenment.</p>
  <div class="lower-band"></div>
  <p class="presenter">Owen Hartley<span class="presenter-date">July 10, 2014</span></p>
  <footer class="footer"><span class="footer-url">www.kelOrvanta.co.uk</span></footer>
</section>

<section class="slide slide--profile">
  <span class="page-number">1</span>
  <h2 class="slide-heading">Owen Hartley</h2>
  <ul class="credential-list">
    <li class="tick">Managing Director Merrow UK</li>
    <li class="tick">CEO Bellcrest Health Co</li>
    <li class="tick">Managing Director Medical and Scientific</li>
    <li class="tick">Director Corvane Market</li>
    <li class="tick">Access/HE/BD/NPP/BI/Training/GA/PA/KAM</li>
  </ul>
  <div class="lower-band"></div>
  <footer class="footer">
    <span class="footer-brand">kelOrvanta</span>
    <span class="footer-url">www.kelOrvanta.co.uk</span>
  </footer>
</section>

<section class="slide slide--mission">
  <span class="page-number">2</span>
  <h2 class="slide-heading">Mission</h2>
  <p class="mission-statement">Deliver cutting edge performance with our clients<br>through the best relationships with customers that<br>influence access to products and services</p>
  <footer class="footer">
    <span class="footer-brand">kelOrvanta</span>
    <span class="footer-url">www.kelOrvanta.co.uk</span>
  </footer>
</section>

<section class="slide slide--values">
  <span class="page-number">3</span>
  <h2 class="slide-heading">Values</h2>
  <div class="value value--energy">
    <div class="value-mark"></div>
    <h3 class="value-name">Energy</h3>
    <ul class="value-traits"><li>Intensity</li><li>Fun</li><li>Determination</li><li>Fortitude</li></ul>
  </div>
  <div class="value value--credibility">
    <div class="value-mark"></div>
    <h3 class="value-name">Credibility</h3>
    <ul class="value-traits"><li>Expertise</li><li>Experience</li><li>Professional</li><li>Constant learning</li></ul>
  </div>
  <div class="value value--relationships">
    <div class="value-mark"></div>
    <h3 class="value-name">Relationships</h3>
    <ul class="value-traits"><li>Networking</li><li>Trust</li><li>Influencing at the top</li></ul>
  </div>
  <footer class="footer">
    <span class="footer-brand">kelOrvanta</span>
    <span class="footer-url">www.kelOrvanta.co.uk</span>
  </footer>
</section>

</body>
</html>
```